Business card with logo for a family psychologist

I need a business card for my private practice in the urban Chicago area as a psychologist. I see families and individuals who are going through difficult times - divorce, separation, illness, or trauma. I want to project hopefulness, competence, and caring.

Target Market(s)

Adults, other professionals - such as physicans and lawyers

Industry/Entity Type

Health Care

Contact Information for Business Card

Front should have my name and credentials; back should have location information including my email, phone

Font styles to use
Serif
Decorative
Script

Requirements
Must have
• Unique logo
Should not have
• No pictures or icons of people; no black

```html
<!DOCTYPE html>
<html lang="en">
<head>
<meta charset="utf-8">
<title>Dr. Laura Bennett – Business Card</title>
<link href="https://fonts.googleapis.com/css2?family=Lato:wght@300;400&family=Pinyon+Script&display=swap" rel="stylesheet">
<style>
  :root {
    --backdrop: #ededed;
    --card: #ffffff;
    --pattern-light: #fafafa;
    --pattern-tone: #ebebeb;
    --gold: #c99a2e;
    --ink: #8a8a8a;
    --ink-soft: #9a9a9a;
    --icon: #a8a8a8;
    --mark-faint: #dcdcdc;
  }
  * { margin: 0; padding: 0; box-sizing: border-box; }
  html, body {
    width: 1200px; height: 1000px; overflow: hidden;
    background: var(--backdrop);
  }
  .canvas { position: relative; width: 1200px; height: 1000px; }

  .card {
    position: absolute; left: 333px; width: 533px;
    background: var(--card);
  }
  .card--front { top: 179px; height: 295px; }
  .card--back { top: 524px; height: 297px; }

  .pattern {
    position: absolute; left: 0; top: 0; width: 100%;
    background: radial-gradient(ellipse at 50% 45%, var(--pattern-light) 0%, var(--pattern-tone) 100%);
  }
  .card--front .pattern { height: 100%; }
  .card--back .pattern { height: 83px; background: var(--pattern-tone); }

  .brand-mark {
    position: absolute; left: 0; width: 100%;
    display: flex; align-items: center; justify-content: center; gap: 12px;
    font-family: 'Lato', sans-serif; font-weight: 400;
  }
  .card--front .brand-mark {
    top: 72px; font-size: 26px; letter-spacing: 0.08em; color: var(--gold);
  }
  .brand-mark .dot { width: 14px; height: 14px; border-radius: 50%; background: currentColor; }

  .practitioner-name {
    position: absolute; left: 0; top: 160px; width: 100%;
    text-align: center;
    font-family: 'Pinyon Script', cursive; font-size: 50px; line-height: 1;
    color: var(--ink);
  }
  .credential {
    position: absolute; left: 0; top: 230px; width: 100%;
    text-align: center;
    font-family: 'Lato', sans-serif; font-weight: 300; font-size: 21px;
    color: var(--ink-soft);
  }

  .card--back .brand-mark {
    left: 40px; top: 170px; width: 135px;
    font-size: 15px; color: var(--mark-faint); letter-spacing: 0.05em;
    flex-direction: column; gap: 6px;
  }

  .contact-list {
    position: absolute; left: 195px; top: 131px;
    list-style: none;
    font-family: 'Lato', sans-serif; font-weight: 300; font-size: 20px;
    color: var(--ink); line-height: 30px;
  }
  .contact-list li { display: flex; align-items: flex-start; gap: 17px; }
  .contact-list .icon { flex: none; width: 22px; height: 22px; margin-top: 4px; }
  .contact-list .icon circle { fill: var(--icon); }
  .contact-list .icon .glyph { fill: none; stroke: #fff; stroke-width: 1.4; }
  .contact-list .icon .glyph-fill { fill: #fff; }
</style>
</head>
<body>
<main class="canvas">

  <section class="card card--front">
    <div class="pattern" role="img" aria-label="Subtle grey diamond lattice pattern"></div>
    <div class="brand-mark"><span class="dot"></span>Dr. Laura Bennett</div>
    <h1 class="practitioner-name">Dr. Laura Bennett</h1>
    <p class="credential">Licensed Clinical Psychologist</p>
  </section>

  <section class="card card--back">
    <div class="pattern" role="img" aria-label="Subtle grey diamond lattice band"></div>
    <div class="brand-mark"><span class="dot"></span>Dr. Laura Bennett</div>
    <ul class="contact-list">
      <li>
        <svg class="icon" viewBox="0 0 22 22" aria-hidden="true">
          <circle cx="11" cy="11" r="11"/>
          <rect class="glyph" x="8" y="5.5" width="6" height="11" rx="1"/>
          <rect class="glyph-fill" x="10.2" y="14" width="1.6" height="1.2"/>
        </svg>
        <span>312 555 0147</span>
      </li>
      <li>
        <svg class="icon" viewBox="0 0 22 22" aria-hidden="true">
          <circle cx="11" cy="11" r="11"/>
          <path class="glyph-fill" d="M11 5 L17 10.5 H15.3 V16 H12.3 V12.5 H9.7 V16 H6.7 V10.5 H5 Z"/>
        </svg>
        <span>240 W. Ontario Suite 905<br>Chicago • Illinois • 60654</span>
      </li>
      <li>
        <svg class="icon" viewBox="0 0 22 22" aria-hidden="true">
          <circle cx="11" cy="11" r="11"/>
          <circle class="glyph" cx="11" cy="11" r="5.5" style="fill:none"/>
          <ellipse class="glyph" cx="11" cy="11" rx="2.3" ry="5.5"/>
          <line class="glyph" x1="5.5" y1="11" x2="16.5" y2="11"/>
        </svg>
        <span>drlaurabennett@mailbox.com</span>
      </li>
    </ul>
  </section>

</main>
</body>
</html>
```